Vexo Systems Web Site Design

Need a basic site to show clients a little about what we do. We are a custom audio video company in the high-end residential market. Need a few basic but professional pages to show past projects and products we sell. No e-commerce. Should include my new logo from ArtHivePro.

Industry/Entity Type

Residential

Number of Pages Required

2 page

Font styles to use
Serif
Sans Serif

Colors
f78f20

Requirements
Must have
• Company Logo, Send feedback page
Nice to have
• I have no ideas about design, but I do know what I like and dislike when I see it.

```html
<!DOCTYPE html>
<html lang="en">
<head>
<meta charset="utf-8">
<title>Vexo Systems</title>
<link rel="stylesheet" href="https://fonts.googleapis.com/css2?family=Lato:wght@300;400;700&display=swap">
<style>
:root{
  --accent:#f78f20;
  --ink:#111111;
  --muted:#555555;
  --field:#ededed;
  --footer:#474747;
  --white:#ffffff;
  --green:#6cb33f;
}
*{margin:0;padding:0;box-sizing:border-box}
html,body{width:1200px;height:2321px;overflow:hidden;background:var(--white);font-family:'Lato',sans-serif;color:var(--ink)}
.page{position:relative;width:1200px;height:2321px}
.nav{position:absolute;top:0;left:0;width:1200px;height:42px;background:var(--white);display:flex;align-items:center}
.brand{position:absolute;left:341px;top:8px;display:flex;align-items:center;gap:6px;font-size:13px;font-weight:700;color:var(--ink)}
.brand-mark{width:22px;height:22px;background:var(--accent)}
.menu{position:absolute;left:530px;top:0;height:42px;display:flex;align-items:center;gap:0;list-style:none;font-size:10px}
.menu li{width:72px;text-align:center;line-height:1.1}
.menu li.active{color:var(--accent)}
.hero{position:absolute;top:42px;left:0;width:1200px;height:473px;background:linear-gradient(180deg,#2a2a30 0%,#3a2f28 45%,#151515 100%)}
.hero-badge{position:absolute;left:511px;top:190px;width:178px;height:102px;border-radius:51px;background:var(--white);display:flex;align-items:center;justify-content:center;gap:8px;font-size:15px;font-weight:700;color:var(--ink)}
.hero-badge .brand-mark{width:30px;height:30px}
.welcome{position:absolute;top:600px;left:0;width:1200px;text-align:center}
.welcome h1{font-size:22px;font-weight:300;letter-spacing:1px;color:var(--ink)}
.welcome p{width:506px;margin:24px auto 0;font-size:10px;line-height:13.5px;text-align:justify;color:var(--ink)}
.services-title{position:absolute;top:816px;left:0;width:1200px;text-align:center;font-size:11px;letter-spacing:.5px}
.tile{position:absolute;top:880px;width:212px;height:220px}
.tile-photo{position:absolute;inset:0}
.tile-label{position:absolute;bottom:10px;left:0;width:100%;text-align:center;color:var(--white);font-size:10px;letter-spacing:1px}
.banner{position:absolute;top:1205px;left:0;width:1200px;height:438px;background:linear-gradient(100deg,#3b2a1d 0%,#6b5240 40%,#8fb3c4 75%,#c7d9e2 100%)}
.banner-text{position:absolute;top:1374px;left:0;width:1200px;text-align:center;color:var(--white);font-size:36px;font-weight:700;line-height:48px}
.contact{position:absolute;top:1730px;left:0;width:1200px;text-align:center}
.contact h2{font-size:21px;font-weight:700}
.contact .sub{font-size:9px;margin-top:2px}
.field-label{position:absolute;left:0;width:1200px;text-align:center;font-size:9px}
.field{position:absolute;left:507px;width:185px;background:var(--field);border:1px solid #d8d8d8}
.submit-rule{position:absolute;left:557px;top:1968px;width:86px;height:1px;background:var(--muted)}
.submit{position:absolute;top:1974px;left:0;width:1200px;text-align:center;font-size:9px}
.footer{position:absolute;top:2133px;left:0;width:1200px;height:188px;background:var(--footer);color:var(--white)}
.f-item{position:absolute;top:52px;display:flex;align-items:center;gap:10px;font-size:8px;line-height:11px}
.f-icon{width:32px;height:32px;border-radius:50%;display:flex;align-items:center;justify-content:center}
.f-company{position:absolute;left:657px;top:60px;font-size:11px;font-weight:700}
.f-company span{color:var(--accent);font-weight:400}
.copyright{position:absolute;top:140px;left:0;width:1200px;text-align:center;font-size:7px}
</style>
</head>
<body>
<div class="page">
  <header class="nav">
    <div class="brand"><span class="brand-mark"></span>Vexo Systems</div>
    <ul class="menu">
      <li>Home</li>
      <li class="active">Products</li>
      <li>Team</li>
      <li class="active">Projects</li>
      <li class="active">Management<br>Login</li>
      <li>Contact</li>
    </ul>
  </header>

  <section class="hero" role="img" aria-label="Close-up photo of a studio mixing console with lit meters">
    <div class="hero-badge"><span class="brand-mark"></span>Vexo Systems</div>
  </section>

  <section class="welcome">
    <h1>WELCOME</h1>
    <p>We design and install custom audio and video systems for fine homes. From private theaters and whole house music to lighting, shades and networks, our team plans every detail with you and your builder. Each system is tuned by hand, built to last and simple to use. We stand behind our work with attentive service long after the final walkthrough, so your home keeps sounding and looking its best for years to come.</p>
  </section>

  <div class="services-title">FEATURED SERVICES</div>
  <div class="tile" style="left:265px">
    <div class="tile-photo" role="img" aria-label="Photo of a home theater room with a large screen" style="background:linear-gradient(160deg,#2b2620,#6f8a99)"></div>
    <div class="tile-label">THEATERS</div>
  </div>
  <div class="tile" style="left:494px">
    <div class="tile-photo" role="img" aria-label="Photo of a bar lounge with wall-mounted screens" style="background:linear-gradient(160deg,#1f1a15,#6a5037)"></div>
    <div class="tile-label">COMMERCIAL</div>
  </div>
  <div class="tile" style="left:722px">
    <div class="tile-photo" role="img" aria-label="Photo of an audio mixing console" style="background:linear-gradient(160deg,#1a1a20,#4a3a4a)"></div>
    <div class="tile-label">AUDIO</div>
  </div>

  <section class="banner" role="img" aria-label="Photo of a luxury home cinema with recliners and a projection screen"></section>
  <div class="banner-text">Audio + Video<br>Anyplace , Anywhere , Anytime</div>

  <section class="contact">
    <h2>Contact us today</h2>
    <p class="sub">Email us below or write to info@vexosystems.com</p>
  </section>
  <div class="field-label" style="top:1810px">Name</div>
  <div class="field" style="top:1827px;height:21px"></div>
  <div class="field-label" style="top:1850px">Email</div>
  <div class="field" style="top:1864px;height:21px"></div>
  <div class="field-label" style="top:1889px">Message</div>
  <div class="field" style="top:1903px;height:54px"></div>
  <div class="submit-rule"></div>
  <div class="submit">Submit</div>

  <footer class="footer">
    <div class="f-item" style="left:283px">
      <span class="f-icon" style="background:var(--accent)">
        <svg width="16" height="16" viewBox="0 0 24 24"><path fill="#fff" d="M6.6 10.8a15 15 0 0 0 6.6 6.6l2.2-2.2c.3-.3.7-.4 1-.2 1.1.4 2.3.6 3.6.6.6 0 1 .4 1 1V20c0 .6-.4 1-1 1A17 17 0 0 1 3 4c0-.6.4-1 1-1h3.5c.6 0 1 .4 1 1 0 1.3.2 2.5.6 3.6.1.3 0 .7-.2 1z"/></svg>
      </span>
      <span>PHONE: (555) 010-0142<br>EMAIL: info@vexosystems.com</span>
    </div>
    <div class="f-item" style="left:476px">
      <span class="f-icon" style="background:var(--green)">
        <svg width="14" height="18" viewBox="0 0 24 30"><path fill="#fff" d="M12 0a10 10 0 0 0-10 10c0 7.5 10 20 10 20s10-12.5 10-20A10 10 0 0 0 12 0zm0 14a4 4 0 1 1 0-8 4 4 0 0 1 0 8z"/></svg>
      </span>
      <span>42 Harbor Lane<br>Townsville, ST</span>
    </div>
    <div class="f-company">VEXO SYSTEMS © 2015 &nbsp;|&nbsp; <span>Privacy Policy</span></div>
    <div class="copyright">© 2015 VEXOSYSTEMS.COM</div>
  </footer>
</div>
</body>
</html>
```